ZB - WESITE NEEDED PAGE: Clean / Modern / Pro & Dynamic

Zephyl-Brokers is a new insurance brokerage firm dealing exclusively with companies (BToB) providing the following property: Liabilities Insurance Insurances Automobile Insurance Insurances Construction% 26amp; Engineering Casualty Workmen 's Compensation Health Insurance Marime% 26amp; Transit Credit Insurance Young, Fast, Proactive and Dynamic we call ourselves Zephyl-Brokers because we are a "start-up" willing to make a difference in the market, bringing modernity and speed to our industry, still too bureaucratic / procedural / opaque uninitiated. We need something respecting the colors of our orange logtype; blue; white; black; easy to scroll, with simple information on the company; - who we are - our team (with the pictures) - what we do - what we do - contact us, contact us (google map) Luanda (Angola) Small company, just need something flashy / professional / structured / modern.

Target Market(s)

BtoB; Oil and gas companies; French speaking copying established in Angola, all industrials, factories and importers of goods.

Industry/Entity Type

Insurance Broker

Font styles to use
Sans Serif

Colors

Requirements
Must have
• We need something respecting the colors of our orange logtype; blue; white; black; easy to scroll, with simple information on the company; - who we are - our team (with the pictures) - what we do - what we do - contact us, contact us (google map) Luanda (Angola) Small company, just need something flashy / professional / structured / modern.
Nice to have
• A page format
Should not have
• WE DO NOT WANT A REFER TO OUR LOGO, but a Home Page for our Website with the basics categories ... >> PLEASE CAREFULLY USE THE RIGHT COLOR OF THE LOGOTYPE which are the ones enclosed Orange / Turquoise / Black as per the business card .

```html
<!DOCTYPE html>
<html lang="en">
<head>
<meta charset="utf-8">
<title>Zephyl-Brokers — Insurance Brokerage, Luanda</title>
<link href="https://fonts.googleapis.com/css2?family=Audiowide&family=Open+Sans:ital,wght@0,400;0,600;0,700;1,400&display=swap" rel="stylesheet">
<style>
:root{
  --orange:#f47b3e;
  --blue:#3ba2df;
  --green:#1b8a3c;
  --ink:#111111;
  --text:#555555;
  --white:#ffffff;
  --footer:#0d0d0d;
}
*{box-sizing:border-box;margin:0;padding:0}
html,body{width:1200px;height:3831px;overflow:hidden}
body{position:relative;background:var(--white);font-family:"Open Sans",sans-serif;color:var(--text)}
.abs{position:absolute}
.backdrop{position:absolute;left:0;top:0}
/* header */
.brand{left:88px;top:82px;font-weight:700;font-size:24px;color:var(--green);letter-spacing:.5px;display:flex;align-items:center;gap:10px}
.brand-dot{width:40px;height:40px;border-radius:50%;background:var(--green);position:absolute;left:68px;top:-64px}
.contact-bar{top:22px;right:92px;display:flex;gap:30px;align-items:center;font-size:17px;color:var(--ink)}
.contact-item{display:flex;align-items:center;gap:12px}
.contact-item.phone{font-weight:600;font-size:19px}
.contact-icon{width:42px;height:42px;border-radius:50%;border:2px solid var(--blue);display:flex;align-items:center;justify-content:center}
.main-nav{top:80px;right:80px;display:flex;gap:50px;font-size:15px;font-weight:700;color:var(--ink)}
.main-nav .active{color:var(--blue)}
/* hero */
.hero-title{top:425px;left:0;width:1200px;text-align:center;font-family:"Audiowide",sans-serif;font-size:76px;color:var(--white)}
.hero-sub{top:518px;left:170px;width:860px;text-align:center;font-size:31px;line-height:40px;color:var(--white)}
.btn{display:inline-flex;align-items:center;gap:8px;border:2px solid var(--orange);border-radius:30px;font-weight:700;font-size:18px}
.btn-hero{top:637px;left:504px;width:192px;height:53px;justify-content:center;background:var(--orange);color:var(--white);border-color:var(--white)}
.btn-ghost{color:var(--orange);background:var(--white)}
.dots{top:742px;left:563px;display:flex;gap:14px}
.dots span{width:14px;height:14px;border-radius:50%;border:2px solid var(--white)}
.dots span.on{background:var(--white)}
/* section headings */
.section-title{font-family:"Audiowide",sans-serif;font-size:40px;color:var(--ink)}
.rocket-mark{width:46px;height:46px}
/* who */
.who-photo{left:95px;top:1005px;width:404px;height:404px;border-radius:50%;background:radial-gradient(circle at 40% 45%,#c8cdd2,#7d8a92);border:14px solid var(--green)}
.who-text{left:587px;top:1110px;width:523px;font-size:16.5px;line-height:30px;text-align:justify}
.who-text p+p{margin-top:14px}
.btn-who{left:587px;top:1373px;width:164px;height:53px;justify-content:center}
/* what we do */
.service{width:488px;height:185px;background:var(--white);border-radius:93px;box-shadow:0 10px 25px rgba(0,0,0,.18)}
.service .ring{position:absolute;top:15px;width:155px;height:155px}
.service h3{position:absolute;top:30px;font-weight:400;font-size:22px;line-height:27px;color:var(--orange)}
.service p{position:absolute;font-size:15.5px;line-height:27px;color:var(--text)}
.service p a{color:var(--orange);text-decoration:none}
.service.left .ring{left:10px}
.service.left h3,.service.left p{left:202px;width:270px}
.service.right .ring{right:10px}
.service.right h3,.service.right p{right:190px;width:280px;text-align:right}
/* team */
.member{width:210px;text-align:center}
.member .photo{width:200px;height:200px;margin:0 auto;border-radius:50%;background:linear-gradient(160deg,#e6e6e6,#9aa0a5);border:8px solid var(--white);box-shadow:10px 0 0 var(--green)}
.member h4{margin-top:18px;font-weight:400;font-size:23px;color:var(--ink)}
.member.featured h4{color:var(--orange)}
.member em{display:block;font-size:16px;color:#888}
.member .socials{display:flex;justify-content:center;gap:14px;margin-top:10px}
.member .socials span{width:9px;height:9px;border-radius:50%;background:#666}
/* footer */
.footer-col{top:3574px;font-size:13.5px;color:var(--white);line-height:21px}
.footer-col h5{font-weight:400;font-size:16.5px;margin-bottom:16px}
.footer-col li{list-style:none}
.news-form{display:flex;margin-top:22px}
.news-form .field{width:192px;height:40px;border:1px solid #333;font-size:11.5px;padding:11px 12px}
.news-form .submit{width:83px;height:40px;background:var(--orange);color:var(--white);font-size:16px;display:flex;align-items:center;justify-content:center}
.social-list li{display:flex;align-items:center;gap:14px;margin-bottom:8px}
.social-list li span{width:8px;height:8px;background:var(--white)}
.copyright{top:3787px;left:0;width:1200px;text-align:center;font-size:12.5px;color:var(--white)}
</style>
</head>
<body>

<svg class="backdrop" width="1200" height="3831" viewBox="0 0 1200 3831" aria-hidden="false">
  <defs>
    <linearGradient id="heroTone" x1="0" y1="0" x2="1" y2="1">
      <stop offset="0" stop-color="#4b5a66"/>
      <stop offset=".5" stop-color="#8a949c"/>
      <stop offset="1" stop-color="#5d6770"/>
    </linearGradient>
    <linearGradient id="blueTone" x1="0" y1="0" x2="1" y2="1">
      <stop offset="0" stop-color="#2f8fd0"/>
      <stop offset=".5" stop-color="#45a9e3"/>
      <stop offset="1" stop-color="#2e92d4"/>
    </linearGradient>
  </defs>
  <!-- hero band -->
  <path fill="var(--orange)" d="M0,275 C300,170 560,110 744,126 C930,140 1080,200 1200,268 L1200,743 C1000,830 760,905 565,903 C360,900 150,830 0,773 Z"/>
  <path role="img" aria-label="Photo of two business people exchanging a contract at a desk" fill="url(#heroTone)" d="M0,293 C300,188 560,128 744,144 C930,158 1080,218 1200,286 L1200,725 C1000,812 760,885 565,885 C360,882 150,812 0,755 Z"/>
  <!-- services band -->
  <path fill="var(--orange)" d="M0,1658 C250,1560 500,1505 670,1509 C900,1515 1080,1580 1200,1650 L1200,2186 C1000,2260 700,2350 490,2350 C300,2350 120,2280 0,2208 Z"/>
  <path role="img" aria-label="Blue tinted photo of a team meeting" fill="url(#blueTone)" d="M0,1676 C250,1578 500,1523 670,1527 C900,1533 1080,1598 1200,1668 L1200,2168 C1000,2242 700,2332 490,2332 C300,2332 120,2262 0,2190 Z"/>
  <!-- map -->
  <rect role="img" aria-label="Road map of Angola centred on Luanda with the office pin" x="0" y="2974" width="1200" height="600" fill="#ececec"/>
  <!-- footer -->
  <path fill="var(--orange)" d="M0,3528 C300,3458 700,3418 1200,3368 L1200,3384 C700,3434 300,3474 0,3544 Z"/>
  <path fill="var(--footer)" d="M0,3542 C300,3472 700,3432 1200,3382 L1200,3831 L0,3831 Z"/>
</svg>

<!-- header -->
<header>
  <div class="abs brand">Zephyl-Brokers</div>
  <div class="abs contact-bar">
    <div class="contact-item phone">
      <span class="contact-icon"><svg width="18" height="18" viewBox="0 0 24 24"><path fill="none" stroke="var(--blue)" stroke-width="2" d="M5 3h4l2 5-3 2a11 11 0 0 0 6 6l2-3 5 2v4a2 2 0 0 1-2 2A17 17 0 0 1 3 5a2 2 0 0 1 2-2z"/></svg></span>
      + 244 900 123 456
    </div>
    <div class="contact-item">
      <span class="contact-icon"><svg width="18" height="18" viewBox="0 0 24 24"><rect x="3" y="6" width="18" height="12" rx="1" fill="var(--blue)"/><path d="M3 7l9 6 9-6" stroke="#fff" stroke-width="1.6" fill="none"/></svg></span>
      info@zephylbrokers.com
    </div>
  </div>
  <nav class="abs main-nav">
    <span class="active">HOME</span><span>ABOUT US</span><span>OUR TEAM</span><span>WHAT WE DO</span><span>CONTACT US</span>
  </nav>
</header>

<!-- hero -->
<section>
  <h1 class="abs hero-title">ZEPHYL-BROKERS</h1>
  <p class="abs hero-sub">Zephyl-Brokers is a new insurance brokerage firm dealing exclusively with companies</p>
  <span class="abs btn btn-hero">Read More
    <svg width="16" height="16" viewBox="0 0 16 16"><circle cx="8" cy="8" r="8" fill="#fff"/><path d="M6 4l4 4-4 4" stroke="var(--orange)" stroke-width="2" fill="none"/></svg></span>
  <div class="abs dots"><span class="on"></span><span></span><span></span></div>
</section>

<!-- who we are -->
<section>
  <div class="abs who-photo" role="img" aria-label="Photo of colleagues working together at a meeting table"></div>
  <svg class="abs rocket-mark" style="left:587px;top:985px" viewBox="0 0 46 46" aria-hidden="true"><path d="M10 36 L36 10" stroke="var(--blue)" stroke-width="6" stroke-linecap="round"/><path d="M8 38 L16 30" stroke="var(--green)" stroke-width="4" stroke-linecap="round"/></svg>
  <h2 class="abs section-title" style="left:587px;top:1038px">Who We Are ?</h2>
  <div class="abs who-text">
    <p>Lorem ipsum dolor sit amet, consectetur adipiscing elit, sed do mod tempor incididunt ut labore et dolore magna aliqua.</p>
    <p>Lorem ipsum dolor sit amet, consectetur adipiscing elit, sed do mod tempor incididunt ut labore et dolore magna aliqua. Ut enim ad minim veniam, quis nostrud exercitation ullamco laboris nisi ut liquip ex ea commodo consequat. Duis aute irure dolor in reprehenderit in tate velit esse cillum dolore eu fugiat nulla pariatur.</p>
  </div>
  <span class="abs btn btn-ghost btn-who">Read More
    <svg width="16" height="16" viewBox="0 0 16 16"><circle cx="8" cy="8" r="8" fill="var(--orange)"/><path d="M6 4l4 4-4 4" stroke="#fff" stroke-width="2" fill="none"/></svg></span>
</section>

<!-- what we do -->
<section>
  <svg class="abs rocket-mark" style="left:577px;top:1636px" viewBox="0 0 46 46" aria-hidden="true"><path d="M10 36 L36 10" stroke="var(--white)" stroke-width="6" stroke-linecap="round"/><path d="M8 38 L16 30" stroke="var(--green)" stroke-width="4" stroke-linecap="round"/></svg>
  <h2 class="abs section-title" style="left:0;width:1200px;text-align:center;top:1686px;color:var(--white)">What We Do ?</h2>

  <article class="abs service left" style="left:89px;top:1774px">
    <svg class="ring" viewBox="0 0 155 155"><path d="M70 8 A70 70 0 1 0 145 90" fill="none" stroke="var(--green)" stroke-width="6"/><path d="M77 45 l22 8 v16 c0 14-10 22-22 26 c-12-4-22-12-22-26 v-16 z M77 58 v22 M66 69 h22" fill="none" stroke="var(--orange)" stroke-width="2.5"/></svg>
    <h3 style="top:30px">Liabilities Insurance</h3>
    <p style="top:68px">Lorem ipsum dolor sit amet, consectetur adipiscing elit, sed do eiusmod tempor...<a>Read More</a></p>
  </article>

  <article class="abs service right" style="left:622px;top:1774px">
    <svg class="ring" viewBox="0 0 155 155"><path d="M85 8 A70 70 0 1 1 10 90" fill="none" stroke="var(--green)" stroke-width="6"/><path d="M72 55 h10 v10 h10 v10 h-10 v10 h-10 v-10 h-10 v-10 h10 z" fill="none" stroke="var(--orange)" stroke-width="2.5"/></svg>
    <h3 style="top:28px">Compensation Health<br>Insurance</h3>
    <p style="top:95px">Lorem ipsum dolor sit amet, tempor incididunt...<a>Read More</a></p>
  </article>

  <article class="abs service left" style="left:89px;top:1979px">
    <svg class="ring" viewBox="0 0 155 155"><path d="M70 8 A70 70 0 1 0 145 90" fill="none" stroke="var(--green)" stroke-width="6"/><path d="M55 80 l6-16 h32 l6 16 v12 h-44 z M62 92 v6 M92 92 v6" fill="none" stroke="var(--orange)" stroke-width="2.5"/></svg>
    <h3 style="top:30px">Automobile Insurance</h3>
    <p style="top:68px">Lorem ipsum dolor sit amet, consectetur adipiscing elit, sed do eiusmod tempor...<a>Read More</a></p>
  </article>

  <article class="abs service right" style="left:622px;top:1979px">
    <svg class="ring" viewBox="0 0 155 155"><path d="M85 8 A70 70 0 1 1 10 90" fill="none" stroke="var(--green)" stroke-width="6"/><rect x="64" y="45" width="26" height="50" rx="4" fill="none" stroke="var(--orange)" stroke-width="2.5"/></svg>
    <h3 style="top:28px">Marime &amp; Transit<br>Credit Insurance</h3>
    <p style="top:95px">Lorem ipsum dolor sit amet, empor incididunt...<a>Read More</a></p>
  </article>
</section>

<!-- team -->
<section>
  <svg class="abs rocket-mark" style="left:577px;top:2450px" viewBox="0 0 46 46" aria-hidden="true"><path d="M10 36 L36 10" stroke="var(--blue)" stroke-width="6" stroke-linecap="round"/><path d="M8 38 L16 30" stroke="var(--green)" stroke-width="4" stroke-linecap="round"/></svg>
  <h2 class="abs section-title" style="left:0;width:1200px;text-align:center;top:2498px">Our Team</h2>
  <div class="abs member" style="left:114px;top:2572px"><div class="photo" role="img" aria-label="Portrait of team member"></div><h4>Lina Moreau</h4><em>Lorem ipsum</em><div class="socials"><span></span><span></span><span></span></div></div>
  <div class="abs member" style="left:368px;top:2572px"><div class="photo" role="img" aria-label="Portrait of team member"></div><h4>Paulo Dias</h4><em>Lorem ipsum</em><div class="socials"><span></span><span></span><span></span></div></div>
  <div class="abs member featured" style="left:622px;top:2572px"><div class="photo" role="img" aria-label="Portrait of team member" style="box-shadow:10px 0 0 var(--green),0 10px 25px rgba(0,0,0,.25)"></div><h4>Sofia Neto</h4><em>Lorem ipsum</em><div class="socials"><span></span><span></span><span></span></div></div>
  <div class="abs member" style="left:876px;top:2572px"><div class="photo" role="img" aria-label="Portrait of team member"></div><h4>Marc Lunel</h4><em>Lorem ipsum</em><div class="socials"><span></span><span></span><span></span></div></div>
</section>

<!-- footer -->
<footer>
  <div class="abs footer-col" style="left:89px">
    <h5>CONTACT US</h5>
    <p>27 Rua das Acácias, Bairro Azul,<br>&nbsp;Luanda (Angola)</p>
    <p style="margin-top:16px;font-size:16px">☏&nbsp;&nbsp;+ 244 900 123 456</p>
    <p style="margin-top:4px">✉&nbsp;&nbsp;info@zephylbrokers.com</p>
  </div>
  <div class="abs footer-col" style="left:412px">
    <h5>QUICK LINKS</h5>
    <ul><li>Home</li><li>About Us</li><li>Our Team</li><li>What we do</li><li>Contact Us</li></ul>
  </div>
  <div class="abs footer-col" style="left:625px;top:3580px">
    <h5>NEWSLETTER</h5>
    <p>Excepteur sint occaecat cupidatat non<br>proident, sunt in culpa qui</p>
    <div class="news-form"><span class="field">Enter your email address</span><span class="submit">Sign Up</span></div>
  </div>
  <div class="abs footer-col" style="left:996px">
    <h5>SOCIAL MEDIA</h5>
    <ul class="social-list"><li><span></span>Friendwall</li><li><span></span>Chirper</li><li><span></span>Circle Plus</li><li><span></span>ClipTube</li></ul>
  </div>
  <p class="abs copyright">© 2019.The Company Name.All Rights Reserved</p>
</footer>

</body>
</html>
```